Medical program Ombo produce by VALORENZA

I need a business card of the program to give to the customer to get the general information to contact the clinic. I need a bilingual card French and English you will see the logo.
That's a program that the Clinic Valorenza offers. https://medicalombo.ca
Program: Ombo Medical Program
Slogan: Lose weight - Exist - Live / Be thin - Exist - Live
The clinic that offers the program: Valorenza
Website: https://medicalombo.ca
---
Medical team / Medical team
email: doc@valorenza.ca
phone: 514 555-0147
Information
email: ombo@valorenza.ca
phone: 514 555-0183 ext 3
Target Market(s)
Every person that needs to lose weight
Industry/Entity Type
Health clinic for obese person
Contact Information for Business Card
All the information in the description
Requirements
Must have
- Look clean - Expensive clinic / Need to be bilingual
Nice to have
- Recto verso for french and english
Should not have
- -

```html
<!DOCTYPE html>
<html lang="fr">
<head>
<meta charset="utf-8">
<title>Ombo Medical Program – Business Cards</title>
<link href="https://fonts.googleapis.com/css2?family=Lato:wght@300;400;700&display=swap" rel="stylesheet">
<style>
  :root {
    --teal: #00b3ad;
    --wave-blue: #0a84d6;
    --brand-blue: #1e8fd5;
    --accent-red: #e8413f;
    --ink: #1d1d1d;
    --white: #ffffff;
    --frame: #3a3a3a;
  }
  * { margin: 0; padding: 0; box-sizing: border-box; }
  html, body { width: 927px; height: 1200px; overflow: hidden; background: var(--white); }
  body { position: relative; font-family: "Lato", Arial, sans-serif; }

  .card {
    position: absolute;
    width: 359px;
    height: 215px;
    border: 0.6px solid var(--frame);
    background: var(--white);
    overflow: hidden;
  }
  .card--fr { left: 83px; top: 176px; }
  .card--en { left: 491px; top: 179px; }

  .card__wave { position: absolute; inset: 0; width: 100%; height: 100%; }

  .clinic {
    position: absolute;
    left: 22px; top: 30px;
    width: 76px;
    text-align: center;
  }
  .clinic__mark {
    display: block;
    width: 16px; height: 16px;
    margin: 0 auto 6px;
    background: var(--accent-red);
  }
  .clinic__name {
    font-size: 11px; font-weight: 700; letter-spacing: 0.6px; color: var(--ink);
    line-height: 1;
  }

  .program {
    position: absolute;
    left: 24px; top: 138px;
    width: 120px;
    font-size: 15px; font-weight: 400; color: var(--brand-blue);
    letter-spacing: 0.5px; line-height: 17px;
  }

  .info {
    position: absolute;
    right: 39px; top: 0;
    text-align: right;
    color: var(--white);
  }
  .info__slogan {
    position: absolute; right: 0; top: 32px;
    font-size: 16px; font-weight: 300; line-height: 17px;
    white-space: nowrap;
  }
  .info__web {
    position: absolute; right: 0; top: 67px;
    font-size: 8.5px; font-weight: 700; white-space: nowrap;
  }
  .info__team {
    position: absolute; right: 0; top: 120px;
    font-size: 9px; font-weight: 400; white-space: nowrap;
  }
  .info__phone {
    position: absolute; right: 0;
    font-size: 12px; font-weight: 400; color: var(--ink); white-space: nowrap;
  }
  .info__phone--main { top: 134px; }
  .info__phone--info { top: 149px; }
  .info__ext {
    position: absolute; right: 0; top: 164px;
    font-size: 6px; color: var(--ink); white-space: nowrap;
  }
  .info__email {
    position: absolute; right: 0;
    font-size: 8.5px; font-weight: 400; color: var(--ink); white-space: nowrap;
  }
  .info__email--doc { top: 171px; }
  .info__email--program { top: 182px; }

  .icon { position: absolute; width: 13px; height: 13px; }
  .icon--phone { right: 21px; top: 138px; }
  .icon--mail { right: 21px; top: 176px; }
</style>
</head>
<body>

  <section class="card card--fr" lang="fr">
    <svg class="card__wave" viewBox="0 0 359 215" aria-hidden="true">
      <path fill="var(--wave-blue)" d="M146,0 C122,30 114,75 144,102 C179,132 189,162 179,192 L170,215 L359,215 L359,0 Z"/>
      <path fill="var(--teal)" d="M152,0 C130,30 124,75 154,100 C189,130 197,160 188,190 L180,215 L359,215 L359,0 Z"/>
    </svg>

    <div class="clinic">
      <span class="clinic__mark"></span>
      <div class="clinic__name">VALORENZA</div>
    </div>

    <div class="program">OMBO MEDICAL PROGRAM</div>

    <div class="info">
      <div class="info__slogan">SE MAIGRIR,<br>ÉXISTER, VIVRE!</div>
      <div class="info__web">www.medicalombo.ca</div>
      <div class="info__team">GROUPE MÉDICAL</div>
      <div class="info__phone info__phone--main">514 555-0147</div>
      <div class="info__phone info__phone--info">514 555-0183</div>
      <div class="info__ext">ext 3</div>
      <div class="info__email info__email--doc">doc@valorenza.ca</div>
      <div class="info__email info__email--program">ombo@valorenza.ca</div>
    </div>

    <svg class="icon icon--phone" viewBox="0 0 14 14" aria-hidden="true">
      <circle cx="7" cy="7" r="6.3" fill="none" stroke="#fff" stroke-width="0.9"/>
      <rect x="4" y="5.5" width="6" height="4.5" rx="0.8" fill="none" stroke="#fff" stroke-width="0.8"/>
      <path d="M3.6,5.2 Q7,2.6 10.4,5.2" fill="none" stroke="#fff" stroke-width="0.8"/>
    </svg>
    <svg class="icon icon--mail" viewBox="0 0 14 14" aria-hidden="true">
      <circle cx="7" cy="7" r="6.3" fill="none" stroke="#fff" stroke-width="0.9"/>
      <rect x="3.8" y="4.8" width="6.4" height="4.6" fill="none" stroke="#fff" stroke-width="0.8"/>
      <path d="M3.8,4.8 L7,7.6 L10.2,4.8 M3.8,9.4 L6,7 M10.2,9.4 L8,7" fill="none" stroke="#fff" stroke-width="0.7"/>
    </svg>
  </section>

  <section class="card card--en" lang="en">
    <svg class="card__wave" viewBox="0 0 359 215" aria-hidden="true">
      <path fill="var(--wave-blue)" d="M146,0 C122,30 114,75 144,102 C179,132 189,162 179,192 L170,215 L359,215 L359,0 Z"/>
      <path fill="var(--teal)" d="M152,0 C130,30 124,75 154,100 C189,130 197,160 188,190 L180,215 L359,215 L359,0 Z"/>
    </svg>

    <div class="clinic">
      <span class="clinic__mark"></span>
      <div class="clinic__name">VALORENZA</div>
    </div>

    <div class="program">OMBO MEDICAL PROGRAM</div>

    <div class="info">
      <div class="info__slogan">LOSE WEIGHT<br>EXIST - LIVE</div>
      <div class="info__web">www.medicalombo.ca</div>
      <div class="info__team">MEDICAL TEAM</div>
      <div class="info__phone info__phone--main">514 555-0147</div>
      <div class="info__phone info__phone--info">514 555-0183</div>
      <div class="info__ext">ext 3</div>
      <div class="info__email info__email--doc">doc@valorenza.ca</div>
      <div class="info__email info__email--program">ombo@valorenza.ca</div>
    </div>

    <svg class="icon icon--phone" viewBox="0 0 14 14" aria-hidden="true">
      <circle cx="7" cy="7" r="6.3" fill="none" stroke="#fff" stroke-width="0.9"/>
      <rect x="4" y="5.5" width="6" height="4.5" rx="0.8" fill="none" stroke="#fff" stroke-width="0.8"/>
      <path d="M3.6,5.2 Q7,2.6 10.4,5.2" fill="none" stroke="#fff" stroke-width="0.8"/>
    </svg>
    <svg class="icon icon--mail" viewBox="0 0 14 14" aria-hidden="true">
      <circle cx="7" cy="7" r="6.3" fill="none" stroke="#fff" stroke-width="0.9"/>
      <rect x="3.8" y="4.8" width="6.4" height="4.6" fill="none" stroke="#fff" stroke-width="0.8"/>
      <path d="M3.8,4.8 L7,7.6 L10.2,4.8 M3.8,9.4 L6,7 M10.2,9.4 L8,7" fill="none" stroke="#fff" stroke-width="0.7"/>
    </svg>
  </section>

</body>
</html>
```